WinterCommuters

First, let me apologize for the short term. We just got an opportunity to place an ad in a commuter newspaper that will run throughout the winter months. We have tropical vacation rentals in Mexico, so it seems worth a shot.

We want to emphasize tropical luxury at competitive prices. Because we will be new to the audience, we need to cover a lot in one ad - images can definitely help. We are supplying photographs - feel free to crop or whatever.

We have the only private complex of luxury houses on the Mexican Caribbean coast, the "Riviera Maya" so we can accommodate anywhere from a single couple to a full wedding party. We want to show our large capacity without scaring off the single couple or small family with mom, dad, and a couple of kids.
Updates

Correction to text:  third paragraph.  The word should be "you", not "so" after "Riviera Maya,"
"As we are in the heart of the Riviera Maya, you will have "

Target Market(s)

Professionals looking to get out of the winter cold. Think tropical!

Industry/Entity Type

Wedding

Requirements
Must have
• The ad must be 5"x5" at 200 DPI (1,000 x 1000 pixels).
• The primary ad will be printed in black and white so it should be saved as a grayscale image. (I think they actually want a jpg, although a tiff would seem more logical!)
• The add will also be on the web in full color so please design the ad with color in mind and then change to grayscale after the content ends.
• Include our logo, phone number, e-mail, and website.
• Also, unless there is a good reason not to, include the four "first tier" images.
• Use the text as provided - not that some is optional.
Nice to have
• Please see the text in the attachments. OOPS: I downloaded the wrong version first - use the most recent "chicagoad" text!
• Also, unless there is a strong reason, use the "first tier" photos. We want to emphasize the accommodations, but also show large groups. We don't want to scare off the smaller groups (couples, small families) with the impression that we are only for large groups.
• The "second tier" photos are available if they would help. Both accommodation and weddings/large groups.
Should not have
• Stock photographs.
• I have (obviously) had some issues loading my files so please forgive the duplicates.

```html
<!DOCTYPE html>
<html lang="en">
<head>
<meta charset="utf-8">
<title>Casa Marisol – Winter Ad</title>
<link href="https://fonts.googleapis.com/css2?family=Ruluko&display=swap" rel="stylesheet">
<style>
  :root{
    --canvas:#ffffff;
    --ink:#2a2a2a;
  }
  .ad--color{
    --frame:#3f5fdc;
    --side:#4466e0;
    --band:#5fe3cf;
    --accent:#2f52d8;
    --label:#f5e84a;
    --paper-a:#fff6cf;
    --paper-b:#ffffff;
    --footer:#64e6cf;
    --footer-ink:#2f52d8;
    --logo-fill:#5fe3cf;
    --logo-ink:#2f52d8;
    --text:#2a2a2a;
    --photo-1a:#6fa9d8; --photo-1b:#2e7a5b;
    --photo-2a:#f2a44a; --photo-2b:#3b2b3d;
    --photo-3a:#e9c76a; --photo-3b:#9a8063;
    --photo-4a:#9fc3e6; --photo-4b:#8c7a66;
  }
  .ad--mono{
    --frame:#7a7a7a;
    --side:#8a8a8a;
    --band:#c2c2c2;
    --accent:#555555;
    --label:#e6e6e6;
    --paper-a:#f4f4f4;
    --paper-b:#ffffff;
    --footer:#c4c4c4;
    --footer-ink:#555555;
    --logo-fill:#cfcfcf;
    --logo-ink:#555555;
    --text:#3a3a3a;
    --photo-1a:#b5b5b5; --photo-1b:#5c5c5c;
    --photo-2a:#bdbdbd; --photo-2b:#3e3e3e;
    --photo-3a:#cacaca; --photo-3b:#808080;
    --photo-4a:#cfcfcf; --photo-4b:#7d7d7d;
  }
  *{box-sizing:border-box;margin:0;padding:0}
  html,body{width:1200px;height:632px;overflow:hidden;background:var(--canvas)}
  body{position:relative;font-family:"Ruluko",sans-serif;color:var(--ink)}
  .ad{
    position:absolute;top:24px;width:564px;height:563px;
    border:3px solid var(--frame);
    background:linear-gradient(135deg,var(--paper-a),var(--paper-b) 55%);
    overflow:hidden;
  }
  .ad--color{left:24px}
  .ad--mono{left:612px}
  .ad__shapes{position:absolute;inset:0}
  .stamp{
    position:absolute;left:10px;width:106px;height:102px;
    border:5px solid #fff;outline:1px dashed #ffffff;outline-offset:2px;
  }
  .stamp--vacations{top:4px;background:linear-gradient(180deg,var(--photo-1a),var(--photo-1b))}
  .stamp--weddings{top:137px;background:linear-gradient(180deg,var(--photo-2a),var(--photo-2b))}
  .stamp--reunions{top:266px;background:radial-gradient(circle,var(--photo-3a) 35%,var(--photo-3b))}
  .stamp--retreats{top:402px;background:linear-gradient(180deg,var(--photo-4a),var(--photo-4b))}
  .stamp-label{position:absolute;left:14px;font-size:19px;color:var(--label);letter-spacing:.3px}
  .stamp-label--vacations{top:111px}
  .stamp-label--weddings{top:243px}
  .stamp-label--reunions{top:372px}
  .stamp-label--retreats{top:506px}
  .tagline{
    position:absolute;left:140px;top:536px;width:530px;height:26px;line-height:26px;
    transform-origin:0 0;transform:rotate(-88.6deg);
    white-space:nowrap;font-size:22px;color:#fff;letter-spacing:.9px;
  }
  .copy{position:absolute;left:190px;top:8px;width:364px;color:var(--text)}
  .headline{font-size:22px;line-height:24px;color:var(--accent);font-weight:400}
  .headline span{color:var(--text)}
  .body{font-size:12.8px;line-height:15.8px;margin:8px 0 0 14px;white-space:nowrap}
  .question{font-size:15.5px;line-height:18px;color:var(--accent);margin-top:10px;white-space:nowrap}
  .question--1{margin-top:6px;margin-left:14px}
  .question--2{margin-left:8px}
  .question--3{margin-left:2px}
  .promise{font-size:18px;line-height:20px;margin-top:10px}
  .invite{font-size:13px;line-height:16px;margin-top:6px;white-space:nowrap}
  .logo{
    position:absolute;left:442px;top:426px;width:108px;height:108px;border-radius:50%;
    background:var(--logo-fill);border:2px solid var(--frame);
    display:flex;align-items:center;justify-content:center;text-align:center;
    font-size:16px;line-height:18px;color:var(--logo-ink);
  }
  .footer{
    position:absolute;left:0;right:0;bottom:0;height:24px;background:var(--footer);
    display:flex;align-items:center;justify-content:center;gap:8px;
    font-size:13px;color:var(--footer-ink);white-space:nowrap;
  }
</style>
</head>
<body>

<section class="ad ad--color" aria-label="Color advertisement">
  <svg class="ad__shapes" width="558" height="557" viewBox="0 0 558 557" aria-hidden="true">
    <path d="M0 0 H144 C138 200 128 380 130 557 H0 Z" fill="var(--side)"/>
    <path d="M144 0 H188 C184 200 178 380 176 557 H130 C128 380 138 200 144 0 Z" fill="var(--band)"/>
  </svg>
  <div class="stamp stamp--vacations" role="img" aria-label="Photo of a pool terrace with palm trees"></div>
  <div class="stamp-label stamp-label--vacations">Vacations</div>
  <div class="stamp stamp--weddings" role="img" aria-label="Photo of a bride on the beach at sunset"></div>
  <div class="stamp-label stamp-label--weddings">Weddings</div>
  <div class="stamp stamp--reunions" role="img" aria-label="Photo of a round banquet table set for a reunion"></div>
  <div class="stamp-label stamp-label--reunions">Reunions</div>
  <div class="stamp stamp--retreats" role="img" aria-label="Photo of a luxury villa courtyard"></div>
  <div class="stamp-label stamp-label--retreats">Retreats</div>
  <div class="tagline">Wouldn't you rather be in a tropical paradise?</div>
  <div class="copy">
    <h1 class="headline">Come and relax in the only<br>private complex of luxury houses on<br>the beautiful Mexican Riviera<span>.</span></h1>
    <p class="body">Only 60 miles South of Cancun, we are a world apart<br>from the noise and crowds of large hotels and party towns.<br>Located in the quiet coastal village of Akumal, you get<br>all of the best amenities, great restaurants, magnificent<br>snorkeling and diving, beaches, and more in the laid back<br>atmosphere that is so hard to find.<br>As we are in the heart of the Riviera Maya, you will have<br>access to shopping, Mayan ruins, tourist attractions, golf,<br>sailing, diving and much more.</p>
    <p class="question question--1">Are you a couple looking for that perfect,<br>secluded getaway?</p>
    <p class="question question--2">Are you looking for a vacation in a quiet,<br>safe, family-friendly area?</p>
    <p class="question question--3">Are you looking to all be together for a wedding,<br>family reunion, or retreat?</p>
    <p class="promise">With 5 luxury homes to choose from,<br>we can meet your exact needs.</p>
    <p class="invite">Visit our web site or call us directly.<br>We look forward to hearing from<br>you and to sharing our homes with<br>you, your family and friends.</p>
  </div>
  <div class="logo">Casa<br>Marisol</div>
  <div class="footer"><span>Mark &amp; Ellen Travis</span>•<span>(555) 014-2290</span>•<span>info@CasaMarisol.com</span>•<span>www.CasaMarisol.com</span></div>
</section>

<section class="ad ad--mono" aria-label="Grayscale advertisement">
  <svg class="ad__shapes" width="558" height="557" viewBox="0 0 558 557" aria-hidden="true">
    <path d="M0 0 H144 C138 200 128 380 130 557 H0 Z" fill="var(--side)"/>
    <path d="M144 0 H188 C184 200 178 380 176 557 H130 C128 380 138 200 144 0 Z" fill="var(--band)"/>
  </svg>
  <div class="stamp stamp--vacations" role="img" aria-label="Photo of a pool terrace with palm trees"></div>
  <div class="stamp-label stamp-label--vacations">Vacations</div>
  <div class="stamp stamp--weddings" role="img" aria-label="Photo of a bride on the beach at sunset"></div>
  <div class="stamp-label stamp-label--weddings">Weddings</div>
  <div class="stamp stamp--reunions" role="img" aria-label="Photo of a round banquet table set for a reunion"></div>
  <div class="stamp-label stamp-label--reunions">Reunions</div>
  <div class="stamp stamp--retreats" role="img" aria-label="Photo of a luxury villa courtyard"></div>
  <div class="stamp-label stamp-label--retreats">Retreats</div>
  <div class="tagline">Wouldn't you rather be in a tropical paradise?</div>
  <div class="copy">
    <h1 class="headline">Come and relax in the only<br>private complex of luxury houses on<br>the beautiful Mexican Riviera<span>.</span></h1>
    <p class="body">Only 60 miles South of Cancun, we are a world apart<br>from the noise and crowds of large hotels and party towns.<br>Located in the quiet coastal village of Akumal, you get<br>all of the best amenities, great restaurants, magnificent<br>snorkeling and diving, beaches, and more in the laid back<br>atmosphere that is so hard to find.<br>As we are in the heart of the Riviera Maya, you will have<br>access to shopping, Mayan ruins, tourist attractions, golf,<br>sailing, diving and much more.</p>
    <p class="question question--1">Are you a couple looking for that perfect,<br>secluded getaway?</p>
    <p class="question question--2">Are you looking for a vacation in a quiet,<br>safe, family-friendly area?</p>
    <p class="question question--3">Are you looking to all be together for a wedding,<br>family reunion, or retreat?</p>
    <p class="promise">With 5 luxury homes to choose from,<br>we can meet your exact needs.</p>
    <p class="invite">Visit our web site or call us directly.<br>We look forward to hearing from<br>you and to sharing our homes with<br>you, your family and friends.</p>
  </div>
  <div class="logo">Casa<br>Marisol</div>
  <div class="footer"><span>Mark &amp; Ellen Travis</span>•<span>(555) 014-2290</span>•<span>info@CasaMarisol.com</span>•<span>www.CasaMarisol.com</span></div>
</section>

</body>
</html>
```